Harold Brisk Mechanical business cards

We need business cards designed for "Harold Brisk Mechanical" "Mechanical & Electrical Contractors" "Specializing in Service & Installation"
"Cooling, Heating, Service, Installations, Residential, Commercial"

```html
<!DOCTYPE html>
<html lang="en">
<head>
<meta charset="utf-8">
<title>Harold Brisk Mechanical – Business Cards</title>
<link rel="stylesheet" href="https://fonts.googleapis.com/css2?family=Montserrat:wght@500;600;700&family=Nunito+Sans:wght@400;600;700&display=swap">
<style>
  :root {
    --brand-red: #e8232b;
    --ink: #1e1e1e;
    --muted: #7a7a7a;
    --icon-grey: #8a8a8a;
    --band-grey: #58595b;
    --paper: #ffffff;
    --bg-top: #ffffff;
    --bg-bottom: #d9dadc;
  }
  * { box-sizing: border-box; margin: 0; padding: 0; }
  html, body { width: 1200px; height: 1200px; overflow: hidden; }
  body {
    background: linear-gradient(180deg, var(--bg-top) 0%, #f1f1f2 55%, var(--bg-bottom) 100%);
    font-family: "Nunito Sans", sans-serif;
    position: relative;
  }
  .card {
    position: absolute;
    left: 180px;
    width: 840px;
    height: 504px;
    border-radius: 20px;
    overflow: hidden;
    box-shadow: 0 6px 18px rgba(0,0,0,0.12);
  }
  .card--front { top: 66px; background: var(--paper); }
  .card--back  { top: 630px; background: var(--brand-red); color: #fff; text-align: center; }

  /* Front */
  .company-mark {
    position: absolute;
    left: 34px; top: 52px;
    width: 290px;
    display: flex; flex-direction: column; align-items: center; gap: 14px;
  }
  .company-mark__square { width: 46px; height: 46px; background: var(--brand-red); }
  .company-mark__name {
    font-family: "Montserrat", sans-serif;
    font-weight: 700;
    font-size: 27px;
    line-height: 1.15;
    color: var(--ink);
    text-align: center;
  }
  .person {
    position: absolute;
    left: 352px; top: 122px;
  }
  .person__name {
    font-family: "Montserrat", sans-serif;
    font-weight: 600;
    font-size: 40px;
    color: var(--ink);
    line-height: 1.1;
  }
  .person__title {
    font-size: 21px;
    color: var(--muted);
    letter-spacing: 0.5px;
    margin-top: 4px;
  }
  .contact { position: absolute; left: 352px; top: 234px; list-style: none; }
  .contact__item {
    display: flex; align-items: flex-start; gap: 12px;
    font-size: 25px; color: var(--ink); line-height: 34px;
    height: 35px;
  }
  .contact__item--address { margin-top: 14px; height: auto; }
  .contact__icon { width: 26px; height: 26px; flex: none; margin-top: 4px; }
  .footer-band {
    position: absolute; left: 0; right: 0; bottom: 0; height: 51px;
    background: var(--band-grey);
  }
  .footer-band__license {
    position: absolute; left: 0; top: 0; bottom: 0; width: 330px;
    background: var(--brand-red);
    clip-path: polygon(0 0, 100% 0, 97% 100%, 0 100%);
    color: #fff; font-size: 19px; line-height: 51px; padding-left: 36px;
  }
  .footer-band__company {
    position: absolute; left: 352px; top: 0;
    color: #fff; font-family: "Montserrat", sans-serif; font-weight: 600;
    font-size: 21px; letter-spacing: 1.6px; line-height: 48px;
  }

  /* Back */
  .back-mark__square {
    width: 84px; height: 84px; background: #fff;
    margin: 76px auto 0;
  }
  .back-mark__name {
    font-family: "Montserrat", sans-serif; font-weight: 600;
    margin-top: 28px;
    line-height: 1;
  }
  .back-mark__line1 { display: block; font-size: 62px; letter-spacing: -1px; }
  .back-mark__line2 { display: block; font-size: 28px; letter-spacing: 14px; margin-top: 18px; padding-left: 14px; }
  .tagline {
    margin-top: 58px;
    font-weight: 700; font-size: 22px;
  }
  .services { margin-top: 6px; font-size: 19px; }
</style>
</head>
<body>

<section class="card card--front" aria-label="Business card front">
  <div class="company-mark">
    <span class="company-mark__square"></span>
    <span class="company-mark__name">Harold Brisk<br>Mechanical</span>
  </div>

  <div class="person">
    <h1 class="person__name">Dale Hutchins</h1>
    <p class="person__title">DIRECTOR</p>
  </div>

  <ul class="contact">
    <li class="contact__item">
      <svg class="contact__icon" viewBox="0 0 26 26" aria-hidden="true"><circle cx="13" cy="13" r="13" fill="var(--icon-grey)"/><rect x="9" y="6" width="8" height="14" rx="1.5" fill="none" stroke="#fff" stroke-width="1.8"/><line x1="11.5" y1="17.5" x2="14.5" y2="17.5" stroke="#fff" stroke-width="1.4"/></svg>
      <span>(555) 214-7730</span>
    </li>
    <li class="contact__item">
      <svg class="contact__icon" viewBox="0 0 26 26" aria-hidden="true"><circle cx="13" cy="13" r="13" fill="var(--icon-grey)"/><path d="M8 7.5c1-.9 2-.8 2.6 0l1.3 2c.4.7.2 1.4-.4 1.9l-.7.6c.7 1.6 2 2.9 3.6 3.6l.6-.7c.5-.6 1.2-.8 1.9-.4l2 1.3c.8.6.9 1.6 0 2.6-1.4 1.5-3.6 1.4-6.3-.7-2.4-1.9-4-4.1-4.8-6-.6-1.7-.5-3.1.2-4.2z" fill="#fff"/></svg>
      <span>(555) 386-1942</span>
    </li>
    <li class="contact__item">
      <svg class="contact__icon" viewBox="0 0 26 26" aria-hidden="true"><circle cx="13" cy="13" r="13" fill="var(--icon-grey)"/><rect x="6.5" y="8.5" width="13" height="9" rx="1" fill="#fff"/><path d="M6.8 9l6.2 5 6.2-5" fill="none" stroke="var(--icon-grey)" stroke-width="1.4"/></svg>
      <span>dale@briskmech.com</span>
    </li>
    <li class="contact__item contact__item--address">
      <svg class="contact__icon" viewBox="0 0 26 26" aria-hidden="true"><circle cx="13" cy="13" r="13" fill="var(--icon-grey)"/><path d="M13 5.5a5.5 5.5 0 0 0-5.5 5.5c0 4 5.5 9.5 5.5 9.5s5.5-5.5 5.5-9.5A5.5 5.5 0 0 0 13 5.5z" fill="#fff"/><circle cx="13" cy="11" r="2" fill="var(--icon-grey)"/></svg>
      <span>418 B Larkspur Suite 3<br>Fenwick, TX 75019</span>
    </li>
  </ul>

  <div class="footer-band">
    <div class="footer-band__license">License #TACLA0012358B</div>
    <div class="footer-band__company">Harold Brisk Mechanical, LLC</div>
  </div>
</section>

<section class="card card--back" aria-label="Business card back">
  <div class="back-mark__square"></div>
  <h2 class="back-mark__name">
    <span class="back-mark__line1">HAROLD BRISK</span>
    <span class="back-mark__line2">MECHANICAL</span>
  </h2>
  <p class="tagline">Specializing in Service &amp; Installation</p>
  <p class="services">Cooling | Heating | Service | Installations | Residential | Commercial</p>
</section>

</body>
</html>
```